Corndell website

Provide a website for a business that is an online farmstand for mostly organic farm products produced on our 9 farms and packaged at our mill. We will be targeting an urban and suburban audience that will be able know the farms where their food is grown and "pick" their food online. We want the site to feel to feel fresh and urbane. Winning logo attached.

The website will feature:

A section with descriptions, pictures and Google maps for the farms as well as the produce produced on each farm. We will want to establish a provenance to the mostly organic food we produce and sell - and visit the farms if they want. We want our customers to know where their food comes from without having to live on a farm. We will market products of local farmers in addition to our own. We'll need room for about 50 farm descriptions and about 5 product descriptions per farm.

A master growing schedule -- there should be room for about 5 products per farm.

An online store (maybe linked to the farm and product) descriptions

An about us section -- where we can tell our family's story and about the history of the mill where we package food and provide fulfillment

A section for links to other farming and food information

A section for legal notices
Updates

Project Deadline Extended
Reason: Holiday weekend for many in USA

Target Market(s)

Educated, urban market who wants quality food at fair prices.

Industry/Entity Type

Farm

```html
<!DOCTYPE html>
<html lang="en">
<head>
<meta charset="utf-8">
<title>Corndell — Online Farmstand</title>
<link href="https://fonts.googleapis.com/css2?family=Fredoka:wght@500;600;700&family=Arimo:wght@400&family=Yanone+Kaffeesatz:wght@300;400&display=swap" rel="stylesheet">
<style>
  :root {
    --green: #7aab17;
    --orange: #fbb43a;
    --orange-deep: #f7a21b;
    --text: #4a4a4a;
    --muted: #8a8a8a;
    --line: #e2e2e2;
    --panel: #f1f1f4;
    --white: #ffffff;
  }
  * { box-sizing: border-box; margin: 0; padding: 0; }
  html, body { width: 1200px; height: 1000px; overflow: hidden; background: var(--white); }
  body { position: relative; font-family: "Fredoka", sans-serif; color: var(--text); }
  .abs { position: absolute; }
  .rule { position: absolute; height: 1px; background: var(--line); }

  .top-note { left: 202px; top: 4px; font-family: "Yanone Kaffeesatz", sans-serif; font-weight: 300; font-size: 15px; color: var(--green); }
  .top-links { right: 118px; top: 5px; font-size: 10px; font-weight: 600; color: #9a9a9a; letter-spacing: .5px; display: flex; gap: 10px; }
  .top-links .divider { width: 1px; height: 16px; background: #ccc; margin-top: -2px; }
  .phone { left: 945px; top: 23px; width: 137px; height: 25px; background: #e8e8e8; border-radius: 0 0 5px 5px; display: flex; align-items: center; justify-content: center; gap: 8px; font-family: "Yanone Kaffeesatz", sans-serif; font-size: 19px; color: #555; }

  .brand { left: 201px; top: 112px; display: flex; align-items: center; gap: 6px; font-size: 22px; font-weight: 700; color: var(--green); letter-spacing: .5px; }
  .brand .mark { width: 11px; height: 11px; background: var(--green); border-radius: 50%; }

  .nav-item { position: absolute; top: 112px; font-size: 10px; font-weight: 600; letter-spacing: .2px; color: #777; white-space: nowrap; }
  .nav-item.active, .foot-item.active { color: var(--green); }

  .map-frame { left: 201px; top: 156px; width: 511px; height: 266px; border: 1px solid var(--line); padding: 6px; }
  .map { width: 100%; height: 100%; background: linear-gradient(135deg, #b3d3f2 0%, #eae6d2 35%, #ece7cc 60%, #b9d6f2 100%); }

  .products-frame { left: 718px; top: 156px; width: 364px; height: 266px; border: 1px solid var(--line); padding: 7px; display: grid; grid-template-columns: repeat(3, 1fr); grid-template-rows: repeat(3, 1fr); gap: 5px; }
  .products-frame .tile { border: 1px solid #ccc; }
  .products-overlay { left: 797px; top: 218px; width: 207px; height: 138px; background: rgba(251, 180, 58, .85); text-align: center; color: var(--white); }
  .products-overlay h2 { margin-top: 24px; font-size: 18px; font-weight: 700; color: #3b3b3b; letter-spacing: 1px; }
  .products-overlay p { margin: 10px 12px 0; font-size: 10px; font-weight: 600; line-height: 16px; letter-spacing: .3px; }
  .products-overlay a { display: inline-block; margin-top: 12px; font-size: 10px; font-weight: 700; color: #333; text-decoration: underline; }

  .feature { left: 201px; top: 432px; width: 290px; height: 216px; background: var(--green); padding: 20px 14px; color: #2f3d0b; }
  .feature h2 { font-size: 14px; font-weight: 700; color: var(--white); letter-spacing: .6px; }
  .feature h3 { margin-top: 12px; font-size: 10px; font-weight: 700; color: var(--white); letter-spacing: .4px; }
  .feature p { margin-top: 12px; font-size: 8.4px; font-weight: 600; line-height: 13px; letter-spacing: .3px; text-transform: uppercase; }
  .btn-orange { display: inline-block; margin-top: 14px; width: 83px; height: 26px; line-height: 26px; text-align: center; background: linear-gradient(#ffcf55, var(--orange-deep)); font-size: 9px; font-weight: 700; color: #4a3200; letter-spacing: .4px; }
  .feature-photo { left: 497px; top: 432px; width: 289px; height: 216px; background: radial-gradient(circle at 40% 55%, #c44b2b 0%, #d97a2a 25%, #9bbf5a 55%, #2f6a1e 90%); }

  .product-card { left: 792px; top: 432px; width: 290px; height: 217px; border: 1px solid #b9d37a; text-align: center; }
  .product-card .shot { position: absolute; left: 88px; top: 34px; width: 96px; height: 110px; background: linear-gradient(#f4f4f4, #cfe0b0); border-radius: 6px; }
  .product-card h4 { position: absolute; left: 0; right: 0; top: 155px; font-size: 10px; font-weight: 700; letter-spacing: .5px; }
  .product-card .sep { position: absolute; left: 20px; right: 20px; top: 173px; height: 1px; background: var(--line); }
  .dots { position: absolute; left: 0; right: 0; top: 181px; display: flex; justify-content: center; gap: 4px; }
  .dots i { width: 13px; height: 13px; border-radius: 50%; background: #ddd; }

  .section-title { font-size: 10.5px; font-weight: 700; letter-spacing: .4px; color: #333; }
  .categories { left: 201px; top: 691px; display: grid; grid-template-columns: 121px 113px 112px 119px 120px; font-family: "Arimo", sans-serif; font-size: 8.6px; line-height: 12.3px; color: var(--muted); }
  .categories .current { color: var(--green); text-decoration: underline; }

  .newsletter { left: 792px; top: 659px; width: 290px; height: 102px; background: linear-gradient(#ffd56a, var(--orange)); padding: 13px 19px; }
  .newsletter .field { margin-top: 13px; display: flex; height: 28px; }
  .newsletter .input { width: 192px; background: var(--white); font-family: "Arimo", sans-serif; font-size: 9px; color: #aaa; padding: 9px 8px; }
  .newsletter .send { width: 64px; margin-left: 2px; background: #f79b0e; display: flex; align-items: center; justify-content: center; }
  .newsletter p { margin-top: 9px; font-family: "Arimo", sans-serif; font-size: 8.2px; color: #4d3500; }

  .about-photo-frame { left: 201px; top: 801px; width: 154px; height: 104px; border: 1px solid var(--line); padding: 5px; }
  .about-photo { width: 100%; height: 100%; background: linear-gradient(160deg, #cfd6de 0%, #8fa3b6 45%, #1a78c8 100%); }
  .about-text { left: 365px; top: 797px; width: 422px; font-size: 7.5px; font-weight: 600; line-height: 16.3px; letter-spacing: .25px; text-transform: uppercase; color: #555; }
  .read-more { left: 367px; top: 893px; font-size: 8.5px; font-weight: 700; color: #888; text-decoration: underline; letter-spacing: .4px; }

  .social { left: 792px; top: 786px; width: 290px; height: 130px; background: var(--panel); text-align: center; }
  .social h3 { margin-top: 18px; font-size: 13px; font-weight: 700; color: #999; letter-spacing: .6px; }
  .social .sep { margin: 8px 16px 0; height: 1px; background: #d6d6da; }
  .social .counts { display: flex; justify-content: center; gap: 12px; margin-top: 10px; margin-left: -24px; }
  .social .stat { width: 36px; text-align: center; }
  .social .count { height: 25px; line-height: 25px; background: var(--white); border: 1px solid #ddd; border-radius: 2px; font-family: "Arimo", sans-serif; font-size: 10px; color: #333; }
  .social .act { margin-top: 8px; height: 17px; line-height: 17px; border-radius: 2px; font-family: "Arimo", sans-serif; font-size: 8px; color: var(--white); font-weight: 700; }
  .act.tweet { background: #26a8e3; }
  .act.like { background: #3b5998; }
  .act.plus { background: #4a4a4a; }

  .foot-item { position: absolute; top: 967px; font-family: "Arimo", sans-serif; font-size: 8.6px; color: #777; white-space: nowrap; }
  .copyright { left: 876px; top: 958px; font-family: "Arimo", sans-serif; font-size: 7.8px; color: #888; }
  .foot-brand { right: 118px; top: 967px; font-size: 12px; font-weight: 700; color: var(--green); letter-spacing: .3px; }
</style>
</head>
<body>
  <div class="abs top-note">Free Shipping</div>
  <div class="abs top-links"><span>LOGIN ▾</span><span class="divider"></span><span>CART: 5 ITEMS</span></div>
  <div class="rule" style="left:201px; top:21px; width:881px;"></div>
  <div class="abs phone">
    <svg width="14" height="14" viewBox="0 0 24 24" aria-hidden="true"><circle cx="12" cy="12" r="11" fill="none" stroke="#444" stroke-width="2"/><path d="M8 6c1 0 1.5 2 2 3l-1.2 1.2c.8 1.8 2.2 3.2 4 4L14 13c1 .5 3 1 3 2s-1 2.5-2.5 2.5C10 17.5 6.5 14 6.5 9 6.5 7.5 7 6 8 6z" fill="#444"/></svg>
    555 014 2286
  </div>

  <div class="abs brand"><span class="mark"></span>CORNDELL</div>
  <nav>
    <span class="nav-item active" style="left:560px;">HOME</span>
    <span class="nav-item" style="left:609px;">SHOP</span>
    <span class="nav-item" style="left:658px;">FARMS</span>
    <span class="nav-item" style="left:707px;">FORUM</span>
    <span class="nav-item" style="left:759px;">EVENTS</span>
    <span class="nav-item" style="left:811px;">NEWSLETTER</span>
    <span class="nav-item" style="left:892px;">BLOGS</span>
    <span class="nav-item" style="left:953px;">GALLERY</span>
    <span class="nav-item" style="left:1018px;">CONTACT US</span>
  </nav>
  <div class="rule" style="left:201px; top:146px; width:881px;"></div>

  <div class="abs map-frame"><div class="map" role="img" aria-label="Map showing the locations of the partner farms"></div></div>

  <div class="abs products-frame">
    <div class="tile" role="img" aria-label="Radishes" style="background:#b83a3a;"></div>
    <div class="tile" role="img" aria-label="Squash blossoms" style="background:#d9a12a;"></div>
    <div class="tile" role="img" aria-label="Ornamental cabbage" style="background:#7d8b8a;"></div>
    <div class="tile" role="img" aria-label="Green citrus" style="background:#9bb038;"></div>
    <div class="tile" role="img" aria-label="Fresh produce" style="background:#c9b24a;"></div>
    <div class="tile" role="img" aria-label="Leafy greens" style="background:#6e7d5a;"></div>
    <div class="tile" role="img" aria-label="Heirloom tomatoes" style="background:#7a4a2e;"></div>
    <div class="tile" role="img" aria-label="Asparagus" style="background:#8e9a6a;"></div>
    <div class="tile" role="img" aria-label="Melons" style="background:#b38a52;"></div>
  </div>
  <div class="abs products-overlay">
    <h2>PRODUCTS</h2>
    <p>LOREM IPSUM DOLOR SIT AMET, CON SECTETUR ADIPISICING ELIT, SED DO</p>
    <a>VIEW ALL</a>
  </div>

  <div class="abs feature">
    <h2>HEADING</h2>
    <h3>SUB HEADING</h3>
    <p>Lorem ipsum dolor sit amet, consectetur adipisicing elit, sed do eiusmod tempor incididunt ut labore et dolore magna aliqua. Ut enim ad minim veniam, quis nostrud exercitation ullamco laboris nisi ut aliquip ex ea commodo consequat. Duis aute irure dolor in reprehenderit in voluptate velit esse cillum dolore eu fugiat nulla pariatur.</p>
    <span class="btn-orange">READ MORE</span>
  </div>
  <div class="abs feature-photo" role="img" aria-label="Pumpkins, apples and fresh corn"></div>

  <div class="abs product-card">
    <div class="shot" role="img" aria-label="Two bottles of organic plant feed"></div>
    <h4>HEADING</h4>
    <div class="sep"></div>
    <div class="dots"><i></i><i></i><i></i><i></i><i></i></div>
  </div>

  <div class="rule" style="left:201px; top:659px; width:585px;"></div>
  <div class="abs section-title" style="left:201px; top:672px;">STORE CATEGORIES</div>
  <div class="abs categories">
    <span class="current">Lorem ipsum dolor (30)</span><span>Lorem ipsum dolor (29)</span><span>Lorem ipsum dolor (40)</span><span>Lorem ipsum dolor (89)</span><span>Lorem ipsum dolor (77)</span>
    <span>Lorem ipsum (10)</span><span>Lorem ipsum (10)</span><span>Lorem ipsum (40)</span><span>Lorem ipsum (70)</span><span>Lorem ipsum (89)</span>
    <span>Lorem ipsum dolor (20)</span><span>Lorem ipsum dolor (20)</span><span>Lorem ipsum dolor (50)</span><span>Lorem ipsum dolor (80)</span><span>Lorem ipsum dolor (78)</span>
    <span>Lorem ipsum olor (30)</span><span>Lorem ipsum olor (30)</span><span>Lorem ipsum olor (60)</span><span>Lorem ipsum olor (90)</span><span>Lorem ipsum olor (55)</span>
    <span>Lorem ipsum dolor (40)</span><span>Lorem ipsum dolor (40)</span><span>Lorem ipsum dolor (70)</span><span>Lorem ipsum dolor(100)</span><span>Lorem ipsum dolor (77)</span>
  </div>

  <div class="abs newsletter">
    <div class="section-title">NEWSLETTER SIGN UP</div>
    <div class="field">
      <div class="input">email@example.com</div>
      <div class="send"><svg width="24" height="17" viewBox="0 0 24 17" aria-hidden="true"><rect x="1" y="1" width="22" height="15" rx="2" fill="#fff3dc" stroke="#c97a00"/><path d="M1 2l11 8 11-8" fill="none" stroke="#c97a00" stroke-width="1.2"/></svg></div>
    </div>
    <p>Lorem ipsum dolor sit amet, consectetur adipisicing elit</p>
  </div>

  <div class="rule" style="left:201px; top:761px; width:585px;"></div>
  <div class="abs section-title" style="left:201px; top:777px;">ABOUT US</div>
  <div class="abs about-photo-frame"><div class="about-photo" role="img" aria-label="Puzzle pieces fitting together"></div></div>
  <p class="abs about-text">Lorem ipsum dolor sit amet, consectetur adipisicing elit, sed do eiusmod tempor incididunt ut labore et dolore magna aliqua. Ut enim ad minim veniam, quis nostrud exercitation ullamco laboris nisi ut aliquip ex ea commodo consequat. Duis aute irure dolor in reprehenderit in voluptate velit esse cillum dolore eu fugiat nulla pariatur. Excepteur sint occaecat cupida tat non proident, sunt in culpa qui officia deserunt mollit anim id est laborum.</p>
  <span class="abs read-more">READ MORE....</span>

  <div class="abs social">
    <h3>SOCIAL LINKS</h3>
    <div class="sep"></div>
    <div class="counts">
      <div class="stat"><div class="count">868</div><div class="act tweet">Tweet</div></div>
      <div class="stat"><div class="count">1.3K</div><div class="act like">Like</div></div>
      <div class="stat"><div class="count">28</div><div class="act plus">+1</div></div>
    </div>
  </div>

  <div class="rule" style="left:201px; top:940px; width:881px;"></div>
  <nav>
    <span class="foot-item active" style="left:201px;">HOME</span>
    <span class="foot-item" style="left:251px;">SHOP</span>
    <span class="foot-item" style="left:300px;">FARMS</span>
    <span class="foot-item" style="left:349px;">FORUM</span>
    <span class="foot-item" style="left:400px;">EVENTS</span>
    <span class="foot-item" style="left:452px;">NEWSLETTER</span>
    <span class="foot-item" style="left:530px;">BLOGS</span>
    <span class="foot-item" style="left:570px;">GALLERY</span>
    <span class="foot-item" style="left:628px;">CONTACT US</span>
  </nav>
  <div class="abs copyright">Copy Right All Right Reserved.2013</div>
  <div class="abs foot-brand">CORNDELL</div>
</body>
</html>
```